Kick Ass, Edgy, Fun, E commerce Embroidery Company Business Card

Sleek and edgy business card layout. main logo on front with business description (Custom Embroidery, the file is submitted is supposed to look like stitching)
Name, address, phone numbers, social icons (Facebook and Instagram) on back. The card will be black plastic and the front main logo will be printed Spot UV.

Target Market(s)

Small Business Owners

Contact Information for Business Card

Focused, not cluttered and sleek. Modern looking.

Font styles to use
Other font styles liked:
• Very clean and elegant

Colors
acd136

Requirements
Must have
• Custom Embroidery

our Tagline: Every Logo Has A Story - Thread Yours
Nice to have
• Social Icons for Facebook and Instagram
Should not have
• Too much visual noise

```html
<!DOCTYPE html>
<html lang="en">
<head>
<meta charset="utf-8">
<title>Rivet Stitch – Business Card</title>
<link rel="stylesheet" href="https://fonts.googleapis.com/css2?family=Archivo+Black&family=Questrial&display=swap">
<style>
  :root {
    --lime: #acd136;
    --card-dark: #333436;
    --ink: #1f2021;
    --white: #f2f2f2;
    --stage: #232324;
    --muted: #8a8b8d;
  }
  * { box-sizing: border-box; margin: 0; padding: 0; }
  html, body { width: 1200px; height: 1000px; overflow: hidden; }
  body {
    background: var(--stage);
    font-family: "Questrial", sans-serif;
    position: relative;
  }
  .card {
    position: absolute;
    left: 250px;
    width: 700px;
    height: 400px;
    background: var(--lime);
    border-radius: 22px;
    padding: 22px;
  }
  .card--front { top: 70px; }
  .card--back { top: 530px; }
  .card__panel {
    position: relative;
    width: 100%;
    height: 100%;
    background: var(--card-dark);
    border-radius: 16px;
    overflow: hidden;
  }

  /* Front */
  .front__brand {
    position: absolute;
    left: 0; right: 0; top: 58px;
    display: flex;
    align-items: center;
    justify-content: center;
    gap: 26px;
  }
  .brand-dot {
    width: 92px; height: 92px;
    border-radius: 50%;
    background: var(--white);
  }
  .front__name {
    font-family: "Archivo Black", sans-serif;
    font-size: 64px;
    line-height: 0.92;
    color: var(--white);
    letter-spacing: 1px;
  }
  .front__band {
    position: absolute;
    left: 0; right: 0; bottom: 58px;
    height: 96px;
    background: var(--lime);
    display: flex;
    flex-direction: column;
    justify-content: center;
    padding-left: 40px;
    font-family: "Archivo Black", sans-serif;
    font-size: 25px;
    line-height: 1.25;
    letter-spacing: 0.5px;
  }
  .front__tagline { color: var(--white); }
  .front__tagline-end { color: var(--ink); }

  /* Back */
  .back__socials {
    position: absolute;
    left: 32px; top: 40px;
    display: flex;
    flex-direction: column;
    gap: 22px;
  }
  .social-dot {
    width: 62px; height: 62px;
    border-radius: 50%;
    background: var(--lime);
  }
  .back__details {
    position: absolute;
    left: 128px; top: 36px;
    color: var(--white);
    font-size: 19px;
    line-height: 1.35;
  }
  .back__company {
    color: var(--lime);
    font-size: 22px;
    letter-spacing: 0.5px;
  }
  .back__contacts { margin-top: 26px; list-style: none; }
  .back__contacts li {
    display: flex;
    align-items: center;
    gap: 12px;
    margin-bottom: 8px;
  }
  .back__contacts svg { width: 20px; height: 20px; flex: none; }
  .hl { color: var(--lime); }
  .back__brand {
    position: absolute;
    right: 34px; bottom: 34px;
    display: flex;
    flex-direction: column;
    align-items: flex-end;
    gap: 16px;
  }
  .back__name {
    font-family: "Archivo Black", sans-serif;
    font-size: 38px;
    line-height: 0.95;
    color: var(--lime);
    text-align: right;
  }
  .brand-dot--small { width: 58px; height: 58px; }
</style>
</head>
<body>

  <section class="card card--front" aria-label="Card front">
    <div class="card__panel">
      <div class="front__brand">
        <span class="brand-dot" aria-hidden="true"></span>
        <h1 class="front__name">RIVET<br>STITCH</h1>
      </div>
      <div class="front__band">
        <p class="front__tagline">EVERY LOGO HAS A STORY</p>
        <p class="front__tagline-end">THREAD YOURS</p>
      </div>
    </div>
  </section>

  <section class="card card--back" aria-label="Card back">
    <div class="card__panel">
      <div class="back__socials" aria-label="Social links">
        <span class="social-dot"></span>
        <span class="social-dot"></span>
      </div>
      <div class="back__details">
        <p class="back__company">RIVETSTITCH INC</p>
        <p>4417 Harbor Mill Dr Ste 2</p>
        <p>Fairview, CO 80412</p>
        <ul class="back__contacts">
          <li>
            <svg viewBox="0 0 20 20" aria-hidden="true"><circle cx="10" cy="10" r="9" fill="none" stroke="#8a8b8d" stroke-width="1.2"/><path d="M7 5.5l2 2-1 1.2a6 6 0 0 0 3.3 3.3l1.2-1 2 2-1.2 1.4c-3.8-.4-7.2-3.8-7.6-7.6z" fill="#8a8b8d"/></svg>
            <span>1800 - 555 - 0187</span>
          </li>
          <li>
            <svg viewBox="0 0 20 20" aria-hidden="true"><circle cx="10" cy="10" r="9" fill="none" stroke="#8a8b8d" stroke-width="1.2"/><rect x="5" y="6.5" width="10" height="7" fill="none" stroke="#8a8b8d" stroke-width="1.2"/><path d="M5 6.5l5 4 5-4" fill="none" stroke="#8a8b8d" stroke-width="1.2"/></svg>
            <span>info<span class="hl">@rivetstitch</span>.com</span>
          </li>
          <li>
            <svg viewBox="0 0 20 20" aria-hidden="true"><circle cx="10" cy="10" r="9" fill="none" stroke="#8a8b8d" stroke-width="1.2"/><circle cx="10" cy="10" r="5" fill="none" stroke="#8a8b8d" stroke-width="1.2"/><path d="M5 10h10M10 5c-2 3-2 7 0 10M10 5c2 3 2 7 0 10" fill="none" stroke="#8a8b8d" stroke-width="1"/></svg>
            <span>www.<span class="hl">rivetstitch</span>.com</span>
          </li>
        </ul>
      </div>
      <div class="back__brand">
        <p class="back__name">RIVET<br>STITCH</p>
        <span class="brand-dot brand-dot--small" aria-hidden="true"></span>
      </div>
    </div>
  </section>

</body>
</html>
```